Business Card Re-Design/Update

We'd like to update out business cards. I've included our current "Style guide" which has the colour scheme of the organisation in it. I've also included the branding files with logos etc in them.

I've also included a copy of one of our existing cards so that you can see how ugly/dated they look. I'd like a fresh modern corporate look.

Target Market(s)

These are for our clients, potential clients, industry contacts - like all business cards

Contact Information for Business Card

Name
Position
Company Address - Level 1, 52 Copperfield Road, Dunmore Qld 4071
Direct Phone
mobile
Email
Website -www.korvelit.com.au
Logo

Colors

Designer to choose colors to be used in the design.

Requirements
Must have
• Main Logo
• Cards will need to be editable to be able to personalize them for each new employee.
Nice to have
• The MapIT, HandIT, KeepIT would be okay to have if they can be sensibly and professionally added to the look without detracting from the main imagery.
• Maybe they could go on the back of the card? will leave this to your creative discretion as to whether/where they fit.
Should not have
• Should not have decorative or script fonts

```html
<!DOCTYPE html>
<html lang="en">
<head>
<meta charset="utf-8">
<title>korvelIT business card</title>
<link rel="stylesheet" href="https://fonts.googleapis.com/css2?family=Open+Sans:wght@400;600;700&display=swap">
<style>
  :root {
    --brand-red: #c8161e;
    --brand-red-deep: #a30f16;
    --ink: #2b2b2d;
    --ink-soft: #4a4a4d;
    --paper: #f4f4f2;
    --tint: #f0d6d6;
    --stage: #e2e2e0;
    --white: #ffffff;
  }
  * { box-sizing: border-box; margin: 0; padding: 0; }
  html, body {
    width: 1200px; height: 900px; overflow: hidden;
    background: var(--stage);
    font-family: "Open Sans", Arial, sans-serif;
  }
  .sheet {
    width: 1200px; height: 900px;
    display: flex; flex-direction: column;
    align-items: center; justify-content: center; gap: 40px;
  }
  .card {
    position: relative; overflow: hidden;
    width: 620px; height: 380px;
    box-shadow: 0 10px 30px rgba(0,0,0,.18);
  }
  /* front */
  .card-front { background: var(--paper); color: var(--ink); }
  .front-mark {
    position: absolute; right: -60px; bottom: -70px;
    width: 300px; height: 300px; background: var(--tint); opacity: .7;
  }
  .wordmark { display: flex; align-items: center; gap: 14px; }
  .wordmark-square { width: 34px; height: 34px; background: var(--brand-red); }
  .wordmark-name { font-weight: 600; letter-spacing: -0.5px; }
  .card-front .wordmark { position: absolute; left: 48px; top: 44px; }
  .card-front .wordmark-name { font-size: 46px; color: var(--ink); }
  .person { position: absolute; left: 48px; top: 142px; }
  .person-name { font-size: 24px; font-weight: 700; color: var(--brand-red); line-height: 1.1; }
  .person-role { font-size: 15px; color: var(--ink-soft); margin-top: 4px; }
  .person-rule { width: 44px; height: 1px; background: #9a9a9a; margin: 12px 0 10px; }
  .address { font-size: 14px; color: var(--ink-soft); }
  .contacts { position: absolute; left: 48px; top: 262px; list-style: none; }
  .contact { display: flex; align-items: center; gap: 10px; font-size: 14px; color: var(--ink-soft); line-height: 22px; }
  .contact svg { width: 14px; height: 14px; flex: none; }
  /* back */
  .card-back {
    background: linear-gradient(160deg, var(--brand-red) 0%, var(--brand-red-deep) 100%);
    color: var(--white);
    display: flex; flex-direction: column; align-items: center; justify-content: center; gap: 34px;
  }
  .card-back .wordmark-square { width: 44px; height: 44px; background: var(--white); }
  .card-back .wordmark-name { font-size: 62px; color: var(--white); }
  .services { display: flex; align-items: center; gap: 22px; list-style: none; }
  .service { display: flex; align-items: center; gap: 8px; font-size: 17px; font-weight: 600; }
  .service-square { width: 12px; height: 12px; background: var(--white); }
  .service-divider { width: 1px; height: 26px; background: rgba(255,255,255,.6); transform: rotate(25deg); }
</style>
</head>
<body>
<main class="sheet">

  <section class="card card-front" aria-label="Card front">
    <div class="front-mark" aria-hidden="true"></div>
    <div class="wordmark">
      <span class="wordmark-square"></span>
      <span class="wordmark-name">korvelIT</span>
    </div>
    <div class="person">
      <p class="person-name">Maren Holloway</p>
      <p class="person-role">Business Development Manager</p>
      <div class="person-rule"></div>
      <p class="address">Level 1, 52 Copperfield Road, Dunmore Qld 4071</p>
    </div>
    <ul class="contacts">
      <li class="contact">
        <svg viewBox="0 0 14 14" fill="none" stroke="#c8161e" stroke-width="1.4"><rect x="3.5" y="1" width="7" height="12" rx="1.2"/><line x1="6" y1="11" x2="8" y2="11"/></svg>
        +61 (0)412 555 019
      </li>
      <li class="contact">
        <svg viewBox="0 0 14 14" fill="#c8161e"><path d="M3 1.5l2.2 0 .9 3-1.4 1.1c.7 1.5 1.8 2.6 3.3 3.3l1.1-1.4 3 .9 0 2.2c0 .6-.5 1-1.1 1C5.6 11.6 2.4 8.4 2 2.6c0-.6.4-1.1 1-1.1z"/></svg>
        +61 (0)7 3555 0142
      </li>
      <li class="contact">
        <svg viewBox="0 0 14 14" fill="none" stroke="#c8161e" stroke-width="1.4"><rect x="1" y="3" width="12" height="8.5"/><polyline points="1,3 7,8 13,3"/></svg>
        mholloway@korvelit.com.au
      </li>
      <li class="contact">
        <svg viewBox="0 0 14 14" fill="none" stroke="#c8161e" stroke-width="1.2"><circle cx="7" cy="7" r="5.8"/><ellipse cx="7" cy="7" rx="2.6" ry="5.8"/><line x1="1.2" y1="7" x2="12.8" y2="7"/></svg>
        www.korvelit.com.au
      </li>
    </ul>
  </section>

  <section class="card card-back" aria-label="Card back">
    <div class="wordmark">
      <span class="wordmark-square"></span>
      <span class="wordmark-name">korvelIT</span>
    </div>
    <ul class="services">
      <li class="service"><span class="service-square"></span>MapIT</li>
      <li class="service-divider" aria-hidden="true"></li>
      <li class="service"><span class="service-square"></span>KeepIT</li>
      <li class="service-divider" aria-hidden="true"></li>
      <li class="service"><span class="service-square"></span>HandIT</li>
    </ul>
  </section>

</main>
</body>
</html>
```